Natural Food Packaging - Peanut Butter bars

Name, branding, trade dress for new line of natural/organic peanut based protein bars. The concept its to package a high value natural product for mass consumer consumption.

There will be 2 to 4 flavors initially introduced. Each flavor has a printed film wrapper and shelf display box. The design winner will have first preference for all the packaging work.Think peanut butter chocolate chip, peanut butter with cranberries, coconut, etc.

We are a privately owned, internationally established organic food manufacturer.

This will be a high profile, well recognized project within the industry.

It is an excellent opportunity for a long term business relationship.

Brisco Market(s)

consumers who want a better quality protein bar than they currently buy. Mostly active adults age 18-50

Industry/Entity Type

Business

Requirements
Must have
• A product name/brand and general look and feel. It needs to convey purity, great ingredients/quality, taste and great price.

It needs to have mass appeal...think Brisco and Zipo, not just Verdano Market.
Nice to have
• Package mock up images for 2 or 3 flavors

```html
<!DOCTYPE html>
<html lang="en">
<head>
<meta charset="utf-8">
<title>Grova – Peanut &amp; Banana wrapper</title>
<link rel="stylesheet" href="https://fonts.googleapis.com/css2?family=Roboto+Condensed:wght@400;700&family=Tinos:wght@400;700&display=swap">
<style>
  :root {
    --paper: #ffffff;
    --brand-blue: #4aa9f5;
    --brand-red: #e8140a;
    --claim-red: #ef3b12;
    --ink: #1e1e1e;
    --band-ink: #1a1a1a;
  }
  html, body {
    margin: 0;
    padding: 0;
    width: 1200px;
    height: 600px;
    overflow: hidden;
    background: var(--paper);
  }
  .wrapper {
    position: relative;
    width: 1200px;
    height: 600px;
    background: var(--paper);
    overflow: hidden;
  }
  .wordmark {
    position: absolute;
    left: 0;
    top: 0;
    width: 860px;
    height: 350px;
  }
  .wordmark text {
    font-family: "Roboto Condensed", "Arial Narrow", sans-serif;
    font-weight: 700;
    font-size: 300px;
    fill: var(--ink);
  }
  .trademark {
    position: absolute;
    left: 850px;
    top: 44px;
    font-family: "Roboto Condensed", "Arial", sans-serif;
    font-weight: 700;
    font-size: 24px;
    color: var(--ink);
  }
  .badges {
    position: absolute;
    left: 1018px;
    top: 36px;
    display: flex;
    gap: 26px;
  }
  .badge {
    width: 52px;
    height: 52px;
    border-radius: 50%;
    border: 3px solid var(--ink);
    box-sizing: border-box;
  }
  .claims {
    position: absolute;
    right: 12px;
    top: 132px;
    margin: 0;
    padding: 0;
    list-style: none;
    text-align: right;
    font-family: "Tinos", "Times New Roman", serif;
    font-size: 33px;
    line-height: 40px;
    color: var(--ink);
  }
  .claims .is-red { color: var(--claim-red); }
  .claims .is-blue { color: var(--brand-blue); }
  .tagline {
    position: absolute;
    left: 22px;
    top: 342px;
    margin: 0;
    font-family: "Roboto Condensed", "Arial Narrow", sans-serif;
    font-weight: 400;
    font-size: 52px;
    line-height: 62px;
    color: var(--ink);
    white-space: nowrap;
  }
  .tagline .lead { color: var(--brand-red); }
  .tagline strong { font-weight: 700; }
  .tagline .word-peanut { color: var(--brand-red); }
  .tagline .word-butter { color: var(--brand-blue); }
  .tagline .word-protein { color: var(--ink); }
  .flavour-band {
    position: absolute;
    left: 0;
    top: 418px;
    width: 1200px;
    height: 182px;
    background: var(--brand-blue);
  }
  .flavour-name {
    position: absolute;
    left: 26px;
    top: 30px;
    margin: 0;
    font-family: "Tinos", "Times New Roman", serif;
    font-weight: 700;
    font-size: 88px;
    line-height: 104px;
    letter-spacing: 3px;
    color: var(--paper);
    white-space: nowrap;
  }
  .net-weight {
    position: absolute;
    right: 34px;
    top: 64px;
    margin: 0;
    font-family: "Tinos", "Times New Roman", serif;
    font-weight: 700;
    font-size: 36px;
    color: var(--band-ink);
  }
  .fineprint {
    position: absolute;
    left: 22px;
    top: 152px;
    margin: 0;
    font-family: "Roboto Condensed", "Arial Narrow", sans-serif;
    font-size: 19px;
    color: var(--band-ink);
    white-space: nowrap;
  }
</style>
</head>
<body>
  <main class="wrapper">
    <svg class="wordmark" viewBox="0 0 860 350" aria-label="Grova">
      <text x="22" y="318" textLength="800" lengthAdjust="spacingAndGlyphs">Grova</text>
    </svg>
    <span class="trademark">TM</span>

    <div class="badges">
      <span class="badge" aria-label="Vegan certification badge"></span>
      <span class="badge" aria-label="Gluten-free certification badge"></span>
    </div>

    <ul class="claims">
      <li class="is-red">Gluten-free.</li>
      <li>All natural.</li>
      <li class="is-blue">Omega-3 from flax.</li>
      <li class="is-red">12 grams of protein.</li>
      <li>Good source of fiber.</li>
    </ul>

    <p class="tagline"><span class="lead">Soft and chewy</span> <strong class="word-peanut">Peanut</strong> <strong class="word-butter">Butter</strong> <strong class="word-protein">Protein</strong> bar</p>

    <section class="flavour-band">
      <h1 class="flavour-name">{Peanut &amp; Banana}</h1>
      <p class="net-weight">net wt 2.05 oz</p>
      <p class="fineprint">A product of Such&amp;Such Co. Pty Ltd 2013. All rights reserved. 123 Street Name, Postcode, Country. Generic fineprint.</p>
    </section>
  </main>
</body>
</html>
```